Health Benefits Association Website Design

The Unified Household Wellspring Alliance (UHWA) is an organization formed for the purpose of providing its members better value for selected health benefits and services. Members can use the association benefits either in conjunction with or independently of other medical insurance they may have. Some of the benefits available include discounted dental and vision care and prescription mail order services. There is no limitation on who can join. This membership will be primarily marketed as a way to enhance the value of a fixed benefit health insurance plan although members do not have to have the insurance plan join the association.

We are seeking a design for a website to be used for consumers to get information about membership and for current members to be able to access their benefits. The website should include:

1) A landing page to provide a description of the UHWA

2) A secondary page that can be duplicated that will:
a. Provide a list of benefits
b. Provide a membership enrollment form
c. Provide a member’s only access page
d. Provide a contact page for more information

We are seeking a modern but conservative design that will reflect value, simplicity and good health. The site design will also need to be compatible for use with mobile phones and tablets.

A copy of the association logo is included with the submission. It will also need to be incorporated into the website design. Layouts of similar association websites have also been included for reference.

Target Market(s)

Ages 25 to 65 unmarried, married with no children, professionals, self-employed, active and healthy

Industry/Entity Type

Health And Wellness

Number of Pages Required

2 page

Font styles to use
Sans Serif

Colors

Designer to choose colors to be used in the design.

Requirements
Must have
• UHWA Logo (attached). Use colors from the logo in the website design.
Nice to have
• Graphics, if used, should convey health and fitness and skew toward a diverse array of adults 25 to 40.

```html
<!DOCTYPE html>
<html lang="en">
<head>
<meta charset="utf-8">
<title>Unified Household Wellspring Alliance</title>
<link href="https://fonts.googleapis.com/css2?family=Bitter:wght@400;600&family=Open+Sans:wght@400;600&display=swap" rel="stylesheet">
<style>
:root{
  --yellow:#fdd000;
  --olive:#8e9b4a;
  --olive-soft:#b7bf85;
  --ink:#2e2e2e;
  --text:#444;
  --footer:#3b3b3b;
  --footer-text:#d6d6d6;
  --accent:#f26b4a;
  --social:#3d8fc7;
  --white:#fff;
}
*{margin:0;padding:0;box-sizing:border-box}
html,body{width:667px;height:1200px;overflow:hidden;background:var(--white)}
body{position:relative;font-family:'Open Sans',sans-serif;color:var(--text)}
.abs{position:absolute}

/* header */
.brand{left:64px;top:22px;width:130px;display:flex;align-items:center;gap:6px}
.brand-dot{width:10px;height:10px;border-radius:50%;background:var(--yellow);flex:none}
.brand-name{font-family:'Bitter',serif;font-weight:600;font-size:11px;line-height:14px;color:var(--olive)}
.call-label{left:391px;top:14px;font-size:7.5px;color:var(--ink)}
.phone{left:370px;top:29px;display:flex;align-items:center;gap:6px;font-size:16px;color:var(--olive)}
.follow-label{left:507px;top:14px;font-size:7.5px;color:var(--ink)}
.social{display:flex;gap:6px}
.social span{width:18px;height:18px;border-radius:50%;border:1px solid var(--social);display:block}
.social span.active{background:var(--accent);border-color:var(--accent)}
.header-social{left:506px;top:31px}
.nav{left:0;top:58px;height:36px;width:667px}
.nav a{position:absolute;top:0;height:36px;line-height:30px;font-family:'Bitter',serif;font-size:7.5px;color:var(--ink);text-decoration:none}
.nav a.current{background:var(--yellow);padding:0 9px;font-weight:600}

/* hero */
.hero{left:0;top:94px;width:667px;height:316px;background:linear-gradient(100deg,#4d5a23 0%,#7d8a3a 35%,#a6a64f 55%,#6b6a2d 100%)}
.hero-caption{left:98px;top:198px;width:238px;height:134px;background:rgba(30,28,15,.6);border-right:2px solid var(--yellow);border-bottom:2px solid var(--yellow)}
.hero-title{left:120px;top:208px;font-family:'Bitter',serif;font-weight:400;font-size:31px;line-height:33px;color:var(--white)}
.btn{display:flex;align-items:center;justify-content:center;gap:6px;background:var(--yellow);font-family:'Bitter',serif;color:var(--ink);text-transform:uppercase}
.hero-btn{left:122px;top:284px;width:99px;height:30px;font-size:10px}
.dots{left:305px;top:381px;display:flex;gap:7px}
.dots span{width:5px;height:5px;border-radius:50%;background:var(--white)}
.dots span.on{background:var(--yellow)}

/* welcome */
.welcome-mark{left:0;width:667px;top:460px;text-align:center;font-family:'Bitter',serif;font-size:11px;color:var(--olive)}
.welcome-mark i{display:inline-block;width:8px;height:8px;border-radius:50%;background:var(--yellow);margin-right:6px}
.section-title{left:0;width:667px;text-align:center;font-family:'Bitter',serif;font-weight:400;color:var(--olive)}
.welcome-title{top:518px;font-size:17.5px}
.welcome-copy{text-align:center;font-size:7.6px;line-height:13.4px;color:var(--ink)}
.welcome-copy.first{left:178px;width:311px;top:552px}
.welcome-copy.second{left:163px;width:341px;top:606px}
.welcome-btn{left:293px;top:654px;width:87px;height:26px;font-size:8px;border-bottom:3px solid var(--white);box-shadow:0 2px 0 var(--yellow)}
.divider{left:211px;top:732px;width:252px;height:1px;background:var(--olive-soft)}

/* benefits */
.benefits-title{top:779px;font-size:17px}
.card{top:836px;width:132px;height:136px;box-shadow:0 2px 6px rgba(0,0,0,.15)}
.card.health{left:58px;background:linear-gradient(135deg,#dfeaf1,#c9dbe8 60%,#f1f4f6)}
.card.consumer{left:199px;background:linear-gradient(135deg,#8c9a52,#a4ac6a);border-bottom:3px solid var(--olive)}
.card.travel{left:340px;background:linear-gradient(180deg,#d8dcc7 0%,#8ea06a 45%,#6d8a3f 100%)}
.card.business{left:481px;background:linear-gradient(135deg,#1f3f6a,#5d7ea6 55%,#9fb4cc)}
.card-label{width:132px;text-align:center;font-family:'Bitter',serif;font-size:11px;color:var(--olive)}
.card-overlay{left:199px;top:870px;width:132px;text-align:center;color:var(--white)}
.card-overlay h3{font-family:'Bitter',serif;font-weight:600;font-size:10.5px;margin-bottom:6px}
.card-overlay p{font-size:6.4px;line-height:9.5px;padding:0 20px}

/* footer */
.footer{left:0;top:1022px;width:667px;height:178px;background:var(--footer)}
.footer-brand{left:60px;top:1084px;width:100px;text-align:center;font-family:'Bitter',serif;font-weight:600;font-size:11px;line-height:14px;color:var(--white)}
.rule{width:1px;height:98px;top:1056px;background:#8a8a8a}
.footer-head{font-size:6.2px;font-weight:600;color:var(--white);text-transform:uppercase}
.footer-text{font-size:5.6px;color:var(--footer-text);white-space:nowrap}
.footer-social{left:488px;top:1085px;gap:12px}
.footer-social span{border-color:#4a7fae}
</style>
</head>
<body>

<header>
  <div class="abs brand"><span class="brand-dot"></span><span class="brand-name">Unified Household Wellspring Alliance</span></div>
  <div class="abs call-label">Call us On</div>
  <div class="abs phone">
    <svg width="12" height="12" viewBox="0 0 24 24" aria-hidden="true"><path d="M6.6 10.8a15 15 0 0 0 6.6 6.6l2.2-2.2a1 1 0 0 1 1-.25 11.4 11.4 0 0 0 3.6.57 1 1 0 0 1 1 1V20a1 1 0 0 1-1 1A17 17 0 0 1 3 4a1 1 0 0 1 1-1h3.5a1 1 0 0 1 1 1c0 1.25.2 2.45.57 3.57a1 1 0 0 1-.25 1z" fill="#8e9b4a"/></svg>
    <span>555.014.2290</span>
  </div>
  <div class="abs follow-label">Follow us</div>
  <div class="abs social header-social" aria-label="Social links"><span></span><span></span><span class="active"></span><span></span></div>
  <nav class="abs nav">
    <a class="current" style="left:262px">Home</a>
    <a style="left:312px">News</a>
    <a style="left:346px">Charities</a>
    <a style="left:395px">Benefits</a>
    <a style="left:444px">Enroll</a>
    <a style="left:486px">Members area</a>
    <a style="left:556px">Contact Us</a>
  </nav>
</header>

<section>
  <div class="abs hero" role="img" aria-label="Photo of a woman in a pink running shirt jogging through a sunlit green forest"></div>
  <div class="abs hero-caption"></div>
  <h1 class="abs hero-title">Better Health<br>Services</h1>
  <div class="abs btn hero-btn">Read more <svg width="5" height="7" viewBox="0 0 5 7"><path d="M0 0l5 3.5L0 7z" fill="#2e2e2e"/></svg></div>
  <div class="abs dots"><span></span><span class="on"></span><span></span><span></span><span></span></div>
</section>

<section>
  <div class="abs welcome-mark"><i></i>Unified Household Wellspring Alliance</div>
  <h2 class="abs section-title welcome-title">Welcome to our site</h2>
  <p class="abs welcome-copy first">Welcome to the Unified Household Wellspring Alliance (UHWA). UHWA was started to be part of a senior-focused charitable organization that is different from other organizations with a similar perspective or mission.</p>
  <p class="abs welcome-copy second">UHWA believes a charity should focus on raising money to support its mission, not its leaders. So, none of the UHWA officers or board members receive any compensation.</p>
  <div class="abs btn welcome-btn">Read more <svg width="4" height="6" viewBox="0 0 5 7"><path d="M0 0l5 3.5L0 7z" fill="#2e2e2e"/></svg></div>
  <div class="abs divider"></div>
</section>

<section>
  <h2 class="abs section-title benefits-title">Our Benefits</h2>
  <div class="abs card health" role="img" aria-label="Photo of a smiling doctor with a stethoscope"></div>
  <div class="abs card consumer" role="img" aria-label="Photo of a shopper with a cart in a store aisle, under a green tint"></div>
  <div class="abs card-overlay"><h3>Consumer</h3><p>Welcome to the Unified Household Wellspring Alliance (UHWA). UHWA was started to be par</p></div>
  <div class="abs card travel" role="img" aria-label="Photo of a traveler in a sun hat looking over green hills"></div>
  <div class="abs card business" role="img" aria-label="Photo of a business handshake over a city skyline"></div>
  <div class="abs card-label" style="left:58px;top:982px">Health</div>
  <div class="abs card-label" style="left:340px;top:980px">Travel</div>
  <div class="abs card-label" style="left:481px;top:979px">Business</div>
</section>

<footer>
  <div class="abs footer"></div>
  <div class="abs footer-brand">Unified Household Wellspring Alliance</div>
  <div class="abs rule" style="left:175px"></div>
  <div class="abs footer-head" style="left:204px;top:1063px">Menu</div>
  <div class="abs footer-text" style="left:204px;top:1078px">Home &nbsp;|&nbsp; News &nbsp;|&nbsp; Charities &nbsp;|&nbsp; Benefits &nbsp;|&nbsp; Enroll &nbsp;|&nbsp; Members Area &nbsp;|&nbsp; Contact us</div>
  <div class="abs footer-head" style="left:204px;top:1111px">Contact us</div>
  <div class="abs footer-text" style="left:204px;top:1130px">218 Cedar Hollow Road &nbsp;|&nbsp; Millbrook, VA 20199</div>
  <div class="abs footer-text" style="left:204px;top:1144px">T : 555.013.4478 &nbsp;&nbsp;|&nbsp;&nbsp; E : hello@uhwa-example.org</div>
  <div class="abs rule" style="left:458px"></div>
  <div class="abs footer-head" style="left:491px;top:1063px">Follow us on</div>
  <div class="abs social footer-social" aria-label="Social links"><span></span><span></span><span class="active"></span><span></span></div>
  <div class="abs footer-text" style="left:487px;top:1149px">Copyrights @ 2017 All Rights Reserved</div>
</footer>

</body>
</html>
```